A5 Flyer for mobile App development

We need a double sided flyer design that will need to be printed on A5 sized paper.
The design will be based on a phone/tablet look and feel.

The idea behind the pamphlet is that we show clients that they can have a mobile app white labelled to their company/brand.

The front of the pamphlet will need to look like a front of a phone with a generic mobile app running within the phone.
The phone must not resemble a real phone, however, it should resemble a cartoon look phone - similar to the attached image called "phone.jpg". The mobile app running within the phone needs to have a "drawing/wireframe" look - similar to the "mock.jpg" image attached. The logo part should look like a "placeholder" image - similar to the image named "mocklogo" (look at the far left) attached.

The back of the pamphlet must also be similar, so that when you turn over the pamphlet, it should look like you're turning over a real phone, and you're now the seeing the back of the phone.
The back of the phone should be styled similar to the front. The text and items on the back of the phone are also in the image named "20170503_212415.jpg".

The phone on the pamphlet should not have an outline, meaning that the pamphlet will have rounded corners, giving the phone a shape.

Please send us a message if you're unsure about anything.

Target Market(s)

Businesses that have salons, spa's, beauty clinics, etc.

Industry/Entity Type

Health And Wellness

Font styles to use
Sans Serif
Script

Colors
e34297

Requirements
Must have
• The pamphlet will have rounded corners, giving the phone its look. See attached the image named "pingloom.."
Should not have
• the phone on the pamphlet should not have an outline, meaning that the pamphlet will have rounded corners, giving the phone a shape. Please have a look at the pingloom image attached that demonstrates the cut out lines.

```html
<!DOCTYPE html>
<html lang="en">
<head>
<meta charset="utf-8">
<title>GLOWDESK – App Flyer</title>
<link href="https://fonts.googleapis.com/css2?family=Comfortaa:wght@400;700&family=Montserrat:wght@300;400;700&family=Raleway:wght@300;600&display=swap" rel="stylesheet">
<style>
  :root {
    --page: #ffffff;
    --case-dark: #6a6b6d;
    --case-mid: #8e9092;
    --case-light: #a4a6a8;
    --rim: #c9cacb;
    --back-light: #d6d7d8;
    --back-mid: #c4c5c6;
    --band: #b3b4b5;
    --ink-grey: #6d6e70;
    --ink-soft: #8b8c8e;
    --pink: #e34297;
    --pink-deep: #d81f7f;
    --pink-pale: #f29ac5;
    --green: #4cb848;
    --red: #da2128;
    --white: #ffffff;
  }
  * { box-sizing: border-box; margin: 0; padding: 0; }
  html, body {
    width: 1200px; height: 878px; overflow: hidden;
    background: var(--page);
  }
  .flyer { position: relative; width: 1200px; height: 878px; }

  /* ---------- front of device ---------- */
  .device-front {
    position: absolute; left: 38px; top: 62px; width: 532px; height: 752px;
    border-radius: 42px;
    background: linear-gradient(90deg, var(--case-light) 0%, var(--case-mid) 30%, var(--case-mid) 70%, var(--case-dark) 100%);
  }
  .device-front .rim {
    position: absolute; inset: 16px; border: 4px solid var(--rim); border-radius: 30px;
  }
  .speaker {
    position: absolute; left: 230px; top: 46px; width: 86px; height: 8px;
    border-radius: 4px; background: #55575a;
  }
  .screen {
    position: absolute; left: 40px; top: 74px; width: 456px; height: 576px;
    overflow: hidden;
  }
  .screen-art {
    position: absolute; inset: 0;
    background:
      linear-gradient(115deg, rgba(255,255,255,0.18) 0%, rgba(255,255,255,0) 40%),
      linear-gradient(250deg, var(--pink-pale) 0%, rgba(242,154,197,0) 35%),
      linear-gradient(160deg, var(--pink) 0%, var(--pink-deep) 55%, var(--pink) 100%);
  }
  .placeholder-mark {
    position: absolute; left: 178px; top: 92px; width: 100px; height: 100px;
  }
  .brand-slot {
    position: absolute; left: 0; right: 0; top: 224px;
    font-family: "Raleway", sans-serif; font-weight: 300;
    font-size: 70px; line-height: 56px; color: var(--white);
    text-align: center; letter-spacing: -1px;
  }
  .book-now {
    position: absolute; left: 82px; top: 438px; width: 284px; height: 38px;
    background: var(--green); color: var(--white);
    font-family: "Montserrat", sans-serif; font-weight: 700;
    font-size: 25px; letter-spacing: 0.4em; line-height: 38px;
    text-align: center; padding-left: 0.4em;
  }
  .home-button {
    position: absolute; left: 246px; top: 666px; width: 48px; height: 48px;
    border-radius: 50%; border: 2px solid #4f5153;
  }

  /* ---------- back of device ---------- */
  .device-back {
    position: absolute; left: 628px; top: 64px; width: 528px; height: 750px;
    border-radius: 42px; overflow: hidden;
    background: linear-gradient(90deg, var(--back-mid) 0%, var(--back-light) 100%);
  }
  .device-back .rim {
    position: absolute; inset: 14px; border: 5px solid #e4e5e6; border-radius: 30px; z-index: 2;
  }
  .camera {
    position: absolute; left: 204px; top: 44px; width: 118px; height: 56px;
    border-radius: 28px; border: 3px solid #eeeeee;
    background: linear-gradient(180deg, #c8c9ca, #d9dadb);
  }
  .camera .lens { position: absolute; top: 12px; width: 32px; height: 32px; border-radius: 50%; }
  .camera .lens-main { left: 18px; background: #7f8183; }
  .camera .lens-flash { left: 70px; background: #f3f3f3; }
  .wordmark {
    position: absolute; left: 0; right: 0; top: 154px;
    display: flex; justify-content: center; align-items: center; gap: 12px;
    font-family: "Montserrat", sans-serif; font-weight: 700; font-size: 36px; color: var(--red);
  }
  .wordmark .mark-square { width: 20px; height: 20px; background: var(--red); }
  .offer-band {
    position: absolute; left: 0; right: 0; top: 229px; height: 353px; background: var(--band);
  }
  .price {
    position: absolute; left: 0; right: 0; top: 22px; text-align: center;
    font-family: "Comfortaa", sans-serif; font-weight: 700; color: var(--ink-grey);
  }
  .price .from { font-size: 42px; }
  .price .amount { font-size: 60px; letter-spacing: -2px; }
  .price .period { font-size: 22px; }
  .pitch {
    position: absolute; left: 0; right: 0; top: 90px; text-align: center;
    font-family: "Montserrat", sans-serif; font-weight: 700;
    font-size: 38px; line-height: 40px; letter-spacing: -1px;
    color: var(--ink-soft); text-transform: uppercase;
  }
  .stores {
    position: absolute; left: 0; right: 0; top: 692px;
    display: flex; justify-content: center; gap: 14px;
    font-family: "Comfortaa", sans-serif; font-weight: 700; font-size: 18px; color: var(--ink-grey);
  }
  .stores { top: 628px; }
  .web {
    position: absolute; left: 0; right: 0; top: 676px; text-align: center;
    font-family: "Comfortaa", sans-serif; font-weight: 700; font-size: 20px;
    letter-spacing: 0.16em; color: var(--ink-soft);
  }
</style>
</head>
<body>
<main class="flyer">

  <section class="device-front">
    <div class="rim"></div>
    <div class="speaker"></div>
    <div class="screen">
      <div class="screen-art" role="img" aria-label="Faceted pink low-poly background pattern"></div>
      <svg class="placeholder-mark" viewBox="0 0 100 100" aria-label="Logo placeholder">
        <circle cx="50" cy="50" r="50" fill="#f0a3c9"/>
        <circle cx="40" cy="33" r="6" fill="#e0207f"/>
        <polygon points="24,68 40,44 50,58 60,44 78,68" fill="#e0207f"/>
      </svg>
      <h1 class="brand-slot">YOUR<br>BRAND<br>HERE</h1>
      <div class="book-now">BOOK NOW</div>
    </div>
    <div class="home-button"></div>
  </section>

  <section class="device-back">
    <div class="rim"></div>
    <div class="camera"><span class="lens lens-main"></span><span class="lens lens-flash"></span></div>
    <div class="wordmark"><span class="mark-square"></span>GLOWDESK</div>
    <div class="offer-band">
      <p class="price"><span class="from">from </span><span class="amount">R499</span><span class="period">pm</span></p>
      <p class="pitch">Let your<br>clients book<br>their next<br>appointment<br>using<br>your app</p>
    </div>
    <div class="stores"><span>droidly</span><span>orchid</span></div>
    <p class="web">email:www.lmnopqrstuv.com</p>
  </section>

</main>
</body>
</html>
```